Veridan Support Coordination

My new business involves providing support coordination for QLPC participants that live with a primary psychosocial and/or developmental delay disability, including but not limited to:

- Anxiety
- Depression
- Bipolar
- Borderline Personality Disorder
- Schizophrenia
- Psychosis
- Autisim Spectrum Disorder
- Fetal Alcohol Spectrum Disorder
- Cerebral Palsy
- Intellectual Disability
- Acquired Brain Injury
- Down Syndrome
- Spina Bifida

The following is an example of another company
https://tallowmerebrook.com/

The are basically 3 types of support we offer
- psychosocial recovery coaching
- support coordination
- specialist support coordination

I have attached a copy of my logo, please utilise this colour scheme for website and business cards.

Target Market(s)

See above

Industry/Entity Type

Health Service

Number of Pages Required

5+ page

Font styles to use
Other font styles liked:
• Arial

Colors

Designer to choose only greyscale colors for use in the design.

```html
<!DOCTYPE html>
<html lang="en">
<head>
<meta charset="utf-8">
<title>Veridan Support Coordination</title>
<link href="https://fonts.googleapis.com/css2?family=Raleway:wght@700;800&family=Questrial&display=swap" rel="stylesheet">
<style>
:root{
  --blue:#0a8fd8;
  --blue-dark:#0780c4;
  --green:#84c225;
  --ink:#111111;
  --grey-text:#7a7a7a;
  --field:#ececec;
  --footer:#2d2d2d;
  --white:#ffffff;
}
*{margin:0;padding:0;box-sizing:border-box}
html,body{width:1200px;height:3247px;overflow:hidden}
body{position:relative;background:var(--white);font-family:'Questrial',Arial,sans-serif;color:var(--ink)}
.abs{position:absolute}
.heading{font-family:'Raleway',Arial,sans-serif;font-weight:800}
.hero-band{left:0;top:0;width:1200px;height:749px;background:var(--blue)}
.topbar{left:50px;top:0;width:1100px;height:107px;background:var(--white);border-radius:0 0 32px 32px}
.brand{display:flex;align-items:center;gap:10px;color:var(--blue);font-size:40px;letter-spacing:-0.5px}
.brand-dot{width:34px;height:34px;border-radius:50%;background:var(--green)}
.top-contact{top:20px;font-size:15px;color:var(--blue);display:flex;align-items:center;gap:10px}
.top-contact.phone{font-size:19px;letter-spacing:1px}
.nav{top:70px;left:330px;display:flex;font-size:15px;letter-spacing:1.8px;color:#222}
.nav span{position:absolute;white-space:nowrap}
.nav .active{color:var(--green)}
.hero-title{left:88px;top:222px;font-size:64px;line-height:68px;color:var(--white)}
.hero-sub{left:88px;top:362px;font-size:30px;color:var(--white)}
.btn{display:flex;align-items:center;justify-content:center;border-radius:30px;font-size:17px}
.btn-white{background:var(--white);color:var(--blue)}
.btn-blue{background:var(--blue);color:var(--white)}
.hero-cta{left:88px;top:428px;width:191px;height:48px}
.hero-art{left:454px;top:151px;width:700px;height:436px;border-radius:48% 52% 40% 45%/55% 50% 45% 40%;background:radial-gradient(ellipse at 55% 45%,#eeeaff 0%,#d9d0fb 55%,#7dd3f5 100%)}
.service{top:599px;width:309px;height:297px;background:var(--white);border-radius:28px;box-shadow:0 4px 14px rgba(0,0,0,.08);text-align:center}
.service h3{margin-top:68px;font-family:'Raleway',Arial,sans-serif;font-weight:700;font-size:30px;line-height:36px;height:80px;display:flex;align-items:center;justify-content:center}
.service .btn{width:162px;height:51px;margin:20px auto 0}
.about-photo{left:88px;top:988px;width:467px;height:428px;border-radius:30px;background:linear-gradient(135deg,#c9c3b8,#8b7a66 55%,#4a3d33)}
.about-card{left:445px;top:1034px;width:664px;height:335px;background:var(--green);border-radius:28px;padding:20px 35px 0 40px;color:var(--white)}
.about-card h2{font-size:45px;line-height:58px;margin-bottom:12px}
.about-card p{font-size:15.5px;line-height:29px;text-align:justify}
.about-card .btn{position:absolute;left:40px;top:254px;width:162px;height:51px}
.section-title{width:1200px;text-align:center;font-size:46px}
.serve-photo{width:333px;height:272px;border-radius:28px}
.serve-label{width:333px;text-align:center;font-family:'Raleway',Arial,sans-serif;font-weight:700;font-size:27px}
.view-all{left:519px;top:2269px;width:162px;height:50px}
.touch-title{font-size:46px}
.touch-copy{left:88px;top:2467px;width:441px;font-size:15.5px;line-height:31.5px;color:var(--grey-text);text-align:justify}
.field{background:var(--field);border-radius:28px;font-size:16px;color:#333;padding-left:28px;display:flex;align-items:center}
.field.msg{align-items:flex-start;padding-top:22px;border-radius:34px}
.submit{left:600px;top:2725px;width:161px;height:49px;font-size:18px}
.footer{left:0;top:2855px;width:1200px;height:392px;background:var(--footer);color:var(--white)}
.footer-brand{left:88px;top:2950px;font-size:46px}
.footer h4{font-weight:400;font-size:20px}
.footer-links{font-size:15px;line-height:30.5px}
.social li{list-style:none;display:flex;align-items:center;gap:14px}
.social i{width:9px;height:9px;border-radius:50%;background:var(--blue);display:inline-block}
.copyright{left:0;top:3211px;width:1200px;text-align:center;font-size:11.5px;color:var(--white)}
</style>
</head>
<body>

<div class="abs hero-band"></div>
<header class="abs topbar"></header>
<div class="abs brand" style="left:88px;top:28px;"><span class="brand-dot"></span><span>Veridan</span></div>

<div class="abs top-contact" style="left:716px;">
  <svg width="17" height="13" viewBox="0 0 17 13"><rect x="0.5" y="0.5" width="16" height="12" rx="1.5" fill="#0a8fd8"/><path d="M1 1.5l7.5 6 7.5-6" stroke="#fff" stroke-width="1.4" fill="none"/></svg>
  <span>hello@veridancare.net</span>
</div>
<div class="abs top-contact phone" style="left:922px;">
  <svg width="15" height="15" viewBox="0 0 24 24"><path fill="#0a8fd8" d="M6.6 10.8a15.1 15.1 0 006.6 6.6l2.2-2.2a1 1 0 011-.25 11.4 11.4 0 003.6.57 1 1 0 011 1V20a1 1 0 01-1 1A17 17 0 013 4a1 1 0 011-1h3.5a1 1 0 011 1c0 1.25.2 2.45.57 3.57a1 1 0 01-.25 1z"/></svg>
  <span>+8 555 014 220</span>
</div>

<nav class="abs nav" style="left:0;">
  <span class="active" style="left:330px;">HOME</span>
  <span style="left:423px;">ABOUT US</span>
  <span style="left:552px;">SERVICES</span>
  <span style="left:678px;">SUPPORT</span>
  <span style="left:801px;">CAREER</span>
  <span style="left:913px;">BLOG</span>
  <span style="left:1002px;">CONTACT US</span>
</nav>

<h1 class="abs heading hero-title">Welcome To<br>Veridan</h1>
<div class="abs hero-sub">Support Coordination</div>
<div class="abs btn btn-white hero-cta">Get Started</div>
<div class="abs hero-art" role="img" aria-label="Illustration of a group of people, including a wheelchair user, surrounded by leaves"></div>

<section class="abs service" style="left:132px;">
  <h3>Psychosocial<br>Recovery coaching</h3>
  <div class="btn btn-blue">Read More</div>
</section>
<section class="abs service" style="left:446px;">
  <h3>Support<br>Coordination</h3>
  <div class="btn btn-blue">Read More</div>
</section>
<section class="abs service" style="left:759px;">
  <h3>Specialist Support<br>Coordination</h3>
  <div class="btn btn-blue">Read More</div>
</section>

<div class="abs about-photo" role="img" aria-label="Photo of a team meeting around a table with a wheelchair user"></div>
<section class="abs about-card">
  <h2 class="heading">About Us</h2>
  <p>Lorem ipsum dolor sit amet, consectetur adipiscing elit, sed do eiusmod tempor incididunt ut labore et dolore magna aliqua. Ut enim ad minim veniam, quis nostrud exercitation ullamco laboris nisi ut aliquip ex ea commodo consequat. Duis aute irure dolor in reprehenderit in voluptate velit esse cillum dolore eu fugiat nulla pariatur. Excepteur sint occaecat cupidatat non proident</p>
  <div class="btn btn-white">Read More</div>
</section>

<h2 class="abs heading section-title" style="left:0;top:1492px;">Who We Serve</h2>

<div class="abs serve-photo" style="left:88px;top:1571px;background:linear-gradient(160deg,#f1f1f1,#cfcfcf)" role="img" aria-label="Photo of a woman sitting against a wall, anxious"></div>
<div class="abs serve-label" style="left:88px;top:1855px;">Anxiety</div>
<div class="abs serve-photo" style="left:434px;top:1571px;background:linear-gradient(160deg,#8e8e8e,#2e2e2e)" role="img" aria-label="Photo of a man with his head in his hands, depressed"></div>
<div class="abs serve-label" style="left:434px;top:1855px;">Depression</div>
<div class="abs serve-photo" style="left:776px;top:1571px;background:linear-gradient(160deg,#5a4a3e,#a07a5c)" role="img" aria-label="Photo of a man with overlapping expressions, representing bipolar disorder"></div>
<div class="abs serve-label" style="left:776px;top:1855px;">Bipolar</div>

<div class="abs serve-photo" style="left:88px;top:1920px;background:radial-gradient(circle at 50% 60%,#5c6670,#1e2328)" role="img" aria-label="Photo of a distressed man in a dark room, representing schizophrenia"></div>
<div class="abs serve-label" style="left:88px;top:2204px;">Schizophrenia</div>
<div class="abs serve-photo" style="left:434px;top:1920px;background:linear-gradient(160deg,#d8d8d8,#8a7766)" role="img" aria-label="Photo of a man holding his head in distress, representing psychosis"></div>
<div class="abs serve-label" style="left:434px;top:2204px;">Psychosis</div>
<div class="abs serve-photo" style="left:776px;top:1920px;background:linear-gradient(160deg,#5c8a4e,#c9423a 60%,#3d5a9a)" role="img" aria-label="Photo of a smiling child in a supportive chair at play"></div>
<div class="abs serve-label" style="left:776px;top:2204px;">Cerebral Palsy</div>

<div class="abs btn btn-blue view-all">View All</div>

<h2 class="abs heading touch-title" style="left:88px;top:2396px;">Get In Touch</h2>
<p class="abs touch-copy">Lorem ipsum dolor sit amet, consectetur adipiscing elit, sed domod tempor incididunt ut labore et dolore magna aliqua. Ut enim ad minim veniam, quis nostrud exercitation ullamco laboris nisi ut aliquip ex ea commodo consequat. Duis aute irure dolor in reprehenderit in voluptate velit esse cillum dolore eu fugiat nulla pariatur.</p>

<h2 class="abs heading touch-title" style="left:599px;top:2396px;">Contact Us</h2>
<div class="abs field" style="left:601px;top:2478px;width:245px;height:53px;">Name</div>
<div class="abs field" style="left:860px;top:2478px;width:245px;height:53px;">Email</div>
<div class="abs field" style="left:601px;top:2544px;width:245px;height:53px;">Phone No</div>
<div class="abs field" style="left:860px;top:2544px;width:245px;height:53px;">Subject</div>
<div class="abs field msg" style="left:601px;top:2609px;width:502px;height:105px;">Message</div>
<div class="abs btn btn-blue submit">Submit</div>

<footer class="abs footer"></footer>
<div class="abs brand footer-brand"><span class="brand-dot" style="width:40px;height:40px;"></span><span>Veridan</span></div>
<h4 class="abs" style="left:88px;top:3073px;font-weight:400;font-size:21px;color:#fff;">Contact Us</h4>
<div class="abs" style="left:88px;top:3115px;display:flex;align-items:center;gap:16px;color:#fff;font-size:15px;">
  <svg width="16" height="12" viewBox="0 0 17 13"><rect x="0.5" y="0.5" width="16" height="12" rx="1.5" fill="#fff"/><path d="M1 1.5l7.5 6 7.5-6" stroke="#2d2d2d" stroke-width="1.4" fill="none"/></svg>
  <span>hello@veridancare.net</span>
</div>

<div class="abs footer" style="background:none;top:0;height:0;">
  <h4 class="abs" style="left:483px;top:2907px;">Our Company</h4>
  <ul class="abs footer-links" style="left:484px;top:2952px;list-style:none;">
    <li>Home</li><li>About Us</li><li>Services</li><li>Support</li><li>Career</li><li>Blog</li><li>Contact Us</li>
  </ul>
  <h4 class="abs" style="left:725px;top:2907px;">Other Links</h4>
  <ul class="abs footer-links" style="left:726px;top:2952px;list-style:none;">
    <li>Faq</li><li>Sitemap</li><li>Any Query</li><li>Privacy Policy</li>
  </ul>
  <h4 class="abs" style="left:949px;top:2907px;">Staying in touch</h4>
  <ul class="abs footer-links social" style="left:951px;top:2952px;">
    <li><i></i>Chirpline</li><li><i></i>Forkyard</li><li><i></i>Facewall</li><li><i></i>Snapframe</li>
  </ul>
</div>

<div class="abs copyright">Copyright © 2020 The Company Name. All rights reserved.</div>

</body>
</html>
```